The Regional Coverage Dealer Handbook

I am writing a best practice book for commercial lines insurance brokers. The subtitle is When The Path Bends Keep Walking Onward. So I want a graphic of maybe someone hiking the summit. I posted an example but don't feel limited I just foudn something I liked.

This is a business book

I just mocked up an example. I dont want designers limited by my design. I am looking for juggling to be artistically displayed on the front cover. I incorporated my name into the logo but probably dont want that in my final design. Should just have my name and designations Mark Toldavo, AAi, CWCP

Target Market(s)

Commercial Insurance Agents

Industry/Entity Type

Insurance

Font styles to use
Sans Serif

Colors

Designer to choose only greyscale colors for use in the design.

Requirements
Must have
• Must have the title of the book
The Regional
Coverage Dealer
Handbook

Also the sub title When The Path Bends Keep Walking Onward

My Name on front cover Mark Toldavo, AAI, CWCP

Book Cover should be black. I uploaded a copy of my work comp playbook for my desired color scehme.

My Lantern Logo on front cover and TideMarket logo on back cover
Nice to have
• Color should be black gray adn red using color from my logo.

```html
<!DOCTYPE html>
<html lang="en">
<head>
<meta charset="utf-8">
<title>The Regional Coverage Dealer Handbook — Cover</title>
<link href="https://fonts.googleapis.com/css2?family=Oswald:wght@500;600&family=Roboto+Condensed:ital,wght@1,700&family=Montserrat:wght@400&family=Work+Sans:wght@400&family=Archivo:ital,wght@1,900&display=swap" rel="stylesheet">
<style>
  :root {
    --page-bg: #e9ebee;
    --cover-black: #050505;
    --cover-glow: #4a1f2a;
    --brand-red: #d8322a;
    --white: #ffffff;
    --light-grey: #c9c9c9;
    --mid-grey: #8d8d8d;
    --banner-light: #cfcfcf;
    --banner-dark: #5c5c5c;
  }
  * { margin: 0; padding: 0; box-sizing: border-box; }
  html, body { width: 848px; height: 1200px; overflow: hidden; background: var(--page-bg); }
  .spread { position: relative; width: 848px; height: 1200px; }

  .cover {
    position: absolute; top: 292px; width: 400px; height: 616px; overflow: hidden;
    background: var(--cover-black);
  }
  .cover--front {
    left: 16px;
    background:
      radial-gradient(ellipse 60% 30% at 45% 8%, var(--cover-glow) 0%, rgba(0,0,0,0) 100%),
      linear-gradient(160deg, #1a1a1a 0%, var(--cover-black) 55%);
  }
  .cover--back {
    left: 432px;
    background: linear-gradient(160deg, #1c1c1c 0%, var(--cover-black) 50%);
  }

  /* Front: title */
  .title {
    position: absolute; left: 92px; top: 80px; width: 222px;
    font-family: "Oswald", sans-serif; font-weight: 600; text-transform: uppercase;
    line-height: 0.95; text-align: right;
  }
  .title__lead { display: flex; align-items: flex-end; justify-content: space-between; }
  .title__the { color: var(--brand-red); font-size: 52px; line-height: 0.85; }
  .title__small { color: var(--white); font-size: 29px; line-height: 1; }
  .title__mid { display: block; color: var(--white); font-size: 29px; margin-top: 2px; }
  .title__big { display: block; color: var(--brand-red); font-size: 60px; line-height: 0.92; letter-spacing: 1px; }

  .subtitle-banner {
    position: absolute; left: 116px; top: 215px; width: 218px; height: 26px;
    background: linear-gradient(90deg, var(--banner-dark), var(--banner-light));
    transform: rotate(-3deg);
    display: flex; align-items: center; justify-content: center;
  }
  .subtitle-banner__text {
    font-family: "Roboto Condensed", sans-serif; font-weight: 700; font-style: italic;
    font-size: 9.6px; color: var(--white); white-space: nowrap;
  }
  .subtitle-banner__tail { position: absolute; left: 116px; top: 238px; }

  .illustration {
    position: absolute; left: 100px; top: 272px; width: 200px; height: 230px;
    background: radial-gradient(ellipse 50% 50% at 50% 50%, #8a8a8a 0%, #3a3a3a 55%, rgba(5,5,5,0) 100%);
    border-radius: 50%;
  }
  .illustration--faint {
    left: 120px; top: 460px; width: 200px; height: 180px; opacity: 0.35;
  }

  .author {
    position: absolute; left: 0; right: 0; top: 508px; text-align: center;
    font-family: "Montserrat", sans-serif; font-size: 12px; color: var(--light-grey);
  }
  .brand {
    position: absolute; left: 0; right: 0; top: 550px;
    display: flex; align-items: center; justify-content: center; gap: 8px;
  }
  .brand__dot { width: 10px; height: 10px; border-radius: 50%; background: var(--brand-red); }
  .brand__name {
    font-family: "Montserrat", sans-serif; font-size: 13px; letter-spacing: 3px;
    color: var(--mid-grey); text-transform: uppercase;
  }

  /* Back */
  .award-badge { position: absolute; left: 47px; top: 60px; width: 102px; height: 80px; background: var(--white); }
  .back-headline {
    position: absolute; left: 170px; top: 66px;
    font-family: "Archivo", sans-serif; font-weight: 900; font-style: italic;
    color: var(--brand-red); font-size: 26px; line-height: 1.18;
  }
  .back-copy {
    position: absolute; left: 47px; top: 168px; width: 330px;
    font-family: "Work Sans", sans-serif; font-size: 10.6px; line-height: 15.6px; color: var(--white);
  }
  .back-copy p + p { margin-top: 15px; }
  .partner-name {
    position: absolute; left: 47px; top: 146px; width: 102px; text-align: center;
    font-family: "Work Sans", sans-serif; font-size: 9px; color: var(--light-grey);
  }
</style>
</head>
<body>
<main class="spread">

  <section class="cover cover--front" aria-label="Front cover">
    <h1 class="title">
      <span class="title__lead"><span class="title__the">The</span><span class="title__small">Regional</span></span>
      <span class="title__mid">Coverage Dealer</span>
      <span class="title__big">Handbook</span>
    </h1>
    <div class="subtitle-banner"><span class="subtitle-banner__text">When The Path Bends Keep Walking Onward</span></div>
    <svg class="subtitle-banner__tail" width="28" height="28" viewBox="0 0 28 28" aria-hidden="true">
      <polygon points="0,0 26,0 24,26" fill="#5c5c5c"/>
    </svg>
    <div class="illustration" role="img" aria-label="Grey illustration of a multi-armed figure juggling spheres and cubes"></div>
    <p class="author">Mark Toldavo, AAI, CWCP</p>
    <div class="brand"><span class="brand__dot"></span><span class="brand__name">Lantern Risk Management</span></div>
  </section>

  <section class="cover cover--back" aria-label="Back cover">
    <div class="award-badge" aria-label="Award badge"></div>
    <p class="partner-name">TideMarket</p>
    <h2 class="back-headline">Trust<br>The Process</h2>
    <div class="back-copy">
      <p>Lorem ipsum dolor sit amet, consectetur adipiscing elit, sed do eiusmod tempor incididunt ut labore et dolore magna aliqua. Ut</p>
      <p>Lorem ipsum dolor sit amet, consectetur adipiscing elit, sed do eiusmod tempor incididunt ut labore et dolore magna aliqua. Ut enim ad minim veniam, quis nostrud exercitation ullamco laboris nisi ut aliquip ex ea commodo consequat. Duis aute irure dolor in reprehenderit in voluptate velit esse</p>
      <p>Lorem ipsum dolor sit amet, consectetur adipiscing elit, sed do eiusmod tempor incididunt ut labore et dolore magna aliqua. Ut enim ad minim veniam, quis nostrud exercitation ullamco laboris nisi ut aliquip ex ea commodo consequat. Duis aute irure dolor in reprehenderit in voluptate velit esse cillum dolore eu</p>
    </div>
    <div class="illustration illustration--faint" role="img" aria-label="Faint repeat of the juggling figure illustration"></div>
  </section>

</main>
</body>
</html>
```